Brisk Fixers 24 Postcard Design, Double-Sided

Please read carefully and see attached. Designers that do not follow these instructions will not be selected. Limit ONE design submission per artist. The ONE design submission shall show both the front and the back designs. Designs must comply with the attached dismensions accounting for the bleed area to prevent designs from being cut off during printing. The attached business card and door tag designs have already been created, printed and are in use. The postcard shall be similar in design to the attached business card and door tag. All of the information that you need is attached. The overall size is 4.12" x 6.12" for the front. The back is different, see attached and scale to match template. I would like the Veteran Owned Business logo added as well. It would also be nice to see my photo incorporated somehow. I like the yellow on the door tag. It helps build contrast and pops out. Again, one design submission per designer that shows both the front and the back.

Target Market(s)

Please read all instructions and see attached.

Industry/Entity Type

Requirements
Must have
• Please read all instructions and see attached.
Nice to have
Should not have

```html
<!DOCTYPE html>
<html lang="en">
<head>
<meta charset="utf-8">
<title>Brisk Fixers 24 Handyman Postcard – Front and Back</title>
<link rel="stylesheet" href="https://fonts.googleapis.com/css2?family=Montserrat:ital,wght@0,700;0,800;1,800;1,900&family=Open+Sans:wght@400;700&family=Roboto+Condensed:wght@400;500&display=swap">
<style>
  :root {
    --sky: #b3cff3;
    --ink: #000000;
    --paper: #ffffff;
    --signal-yellow: #fff200;
    --alert-red: #e4161b;
    --text-dark: #1a1a1a;
    --badge-navy: #2b3a7a;
    --badge-red: #d81f26;
  }
  * { box-sizing: border-box; margin: 0; padding: 0; }
  html, body { width: 1200px; height: 2250px; overflow: hidden; }
  body { background: var(--sky); position: relative; font-family: "Open Sans", sans-serif; }

  .card { position: absolute; transform-origin: top left; overflow: hidden; }
  .card-front { left: 94px; top: 51px; width: 1160px; height: 781px; transform: scale(0.8733); background: var(--paper); }
  .card-back { left: 131px; top: 1528px; width: 1170px; height: 787px; transform: scale(0.8734); background: var(--paper); }

  .layer { position: absolute; inset: 0; }
  .abs { position: absolute; }
  .center-x { transform: translateX(-50%); text-align: center; white-space: nowrap; }

  .web-line { font-family: "Montserrat", sans-serif; font-style: italic; font-weight: 800; color: var(--signal-yellow); display: flex; align-items: center; gap: 10px; }
  .brand-title { font-family: "Montserrat", sans-serif; font-style: italic; font-weight: 900; color: var(--signal-yellow); letter-spacing: -1px; line-height: 1; }
  .brand-sub { font-family: "Montserrat", sans-serif; font-style: italic; font-weight: 900; color: var(--signal-yellow); line-height: 1; }
  .title-rule { position: absolute; height: 4px; background: var(--signal-yellow); }

  .brand-mark { position: absolute; border: 4px solid var(--paper); border-radius: 50%; display: flex; align-items: center; justify-content: center; text-align: center; font-family: "Montserrat", sans-serif; font-weight: 800; color: var(--paper); line-height: 1.1; }
  .partner-badge { position: absolute; }

  .owner-photo { position: absolute; border-radius: 50%; border: 6px solid var(--signal-yellow); box-shadow: 0 0 0 4px var(--ink); background: linear-gradient(180deg, #e4e4e4 0%, #c9c9c9 60%, #9fa3a8 100%); }
  .owner-name { font-family: "Open Sans", sans-serif; font-weight: 700; font-size: 25px; color: var(--text-dark); }
  .owner-role { font-family: "Open Sans", sans-serif; font-weight: 400; font-size: 29px; color: var(--text-dark); }

  .section-head { font-family: "Montserrat", sans-serif; font-style: italic; font-weight: 900; color: var(--alert-red); font-size: 40px; line-height: 1; }
  .section-sub { font-family: "Open Sans", sans-serif; font-size: 24px; color: var(--text-dark); }
  .bullet-list { position: absolute; list-style: none; font-family: "Roboto Condensed", sans-serif; font-weight: 500; font-size: 25px; color: var(--text-dark); }
  .bullet-list li { display: flex; align-items: center; height: 45px; }
  .bullet-list li::before { content: ""; width: 9px; height: 9px; background: var(--alert-red); transform: rotate(45deg); margin-right: 14px; flex: none; }

  .cta { font-family: "Montserrat", sans-serif; font-weight: 800; color: var(--paper); line-height: 1; }
  .cta .cta-word { color: var(--alert-red); }
  .contact-line { font-family: "Open Sans", sans-serif; color: var(--paper); display: flex; align-items: center; justify-content: center; gap: 10px; white-space: nowrap; }
  .icon { flex: none; }

  .photo-tile { position: absolute; }
  .tile-welding { background: linear-gradient(135deg, #1d2a3a 0%, #3b4b5e 45%, #7a6a55 70%, #2a2e36 100%); }
  .tile-router { background: linear-gradient(135deg, #6ec3e0 0%, #86d0e8 50%, #5ab4d4 100%); }
  .tile-cables { background: linear-gradient(180deg, #f2f2f2 0%, #d9d9d9 60%, #b7b2aa 100%); }
  .tile-frames { background: linear-gradient(180deg, #f6f4f0 0%, #ece6dc 65%, #c89a6a 100%); }
</style>
</head>
<body>

<!-- FRONT -->
<section class="card card-front" aria-label="Postcard front">
  <svg class="layer" viewBox="0 0 1160 781" width="1160" height="781" aria-hidden="true">
    <polygon points="0,0 1160,0 1160,287 580,392 0,287" fill="#000"/>
    <polygon points="27,272 478,350 478,362" fill="#fff200"/>
    <polygon points="1133,272 686,350 686,362" fill="#fff200"/>
    <polygon points="0,682 582,565 1160,682 1160,781 0,781" fill="#000"/>
    <polygon points="27,695 582,572 1133,695 582,588" fill="#fff200"/>
  </svg>

  <div class="abs web-line center-x" style="left:580px; top:22px; font-size:36px;">
    <svg class="icon" width="38" height="38" viewBox="0 0 40 40" fill="none" stroke="#fff200" stroke-width="3"><circle cx="20" cy="20" r="17"/><ellipse cx="20" cy="20" rx="8" ry="17"/><line x1="3" y1="20" x2="37" y2="20"/><line x1="6" y1="11" x2="34" y2="11"/><line x1="6" y1="29" x2="34" y2="29"/></svg>
    <span>BriskFixers24.com</span>
  </div>
  <div class="abs brand-title center-x" style="left:580px; top:92px; font-size:72px;">BRISK FIXERS 24</div>
  <div class="title-rule" style="left:300px; width:560px; top:170px;"></div>
  <div class="abs brand-sub center-x" style="left:580px; top:184px; font-size:62px;">HANDYMAN</div>

  <div class="brand-mark" style="left:27px; top:25px; width:204px; height:204px; font-size:26px;">BRISK<br>FIXERS 24</div>

  <svg class="partner-badge" style="left:932px; top:22px;" width="210" height="180" viewBox="0 0 210 180" aria-hidden="true">
    <circle cx="105" cy="88" r="82" fill="#fff"/>
    <circle cx="105" cy="88" r="74" fill="#2b3a7a"/>
    <rect x="0" y="90" width="210" height="30" fill="#d81f26"/>
  </svg>

  <div class="owner-photo" role="img" aria-label="Portrait photo of the owner" style="left:477px; top:265px; width:210px; height:210px;"></div>
  <div class="abs owner-name center-x" style="left:582px; top:488px;">Dale R. Hollins</div>
  <div class="abs owner-role center-x" style="left:582px; top:520px;">Owner &amp; Handman</div>

  <div class="abs section-head" style="left:54px; top:362px;">BENEFITS</div>
  <div class="abs section-sub" style="left:54px; top:396px;">of using our services</div>
  <ul class="bullet-list" style="left:54px; top:433px;">
    <li>Fast Response</li>
    <li>High Quality</li>
    <li>Fair Price</li>
    <li>Veteran Owned</li>
  </ul>

  <div class="abs section-head" style="left:746px; top:373px;">SERVICES:</div>
  <ul class="bullet-list" style="left:746px; top:420px;">
    <li>Assembly</li>
    <li>Small Repairs</li>
    <li>Wifi / Router Setup</li>
    <li>Wireless Device Setup</li>
  </ul>
  <ul class="bullet-list" style="left:980px; top:417px;">
    <li>Fabrication</li>
    <li>Hanging Items</li>
    <li>Odd Jobs</li>
  </ul>

  <div class="abs cta center-x" style="left:597px; top:636px; font-size:42px;"><span class="cta-word">TEXT</span> TO INQUIRE</div>
  <div class="abs contact-line center-x" style="left:597px; top:683px; font-size:29px;">
    <svg class="icon" width="26" height="26" viewBox="0 0 26 26"><circle cx="13" cy="13" r="12" fill="#fff"/><path d="M8 7c1-1 2-1 2.6 0l1.2 2c.4.7.2 1.3-.4 1.8l-.8.6c.6 1.6 1.8 2.9 3.4 3.6l.6-.8c.5-.6 1.1-.8 1.8-.4l2 1.2c1 .6 1 1.6 0 2.6-1.3 1.3-3 1.4-5 .3-2.6-1.4-4.5-3.4-5.8-6-1-2-.9-3.6.4-4.9z" fill="#000"/></svg>
    <span>(555) 014 2290</span>
    <svg class="icon" width="24" height="28" viewBox="0 0 24 28" style="margin-left:16px;"><path d="M12 1C6 1 2 5.5 2 11c0 7 10 16 10 16s10-9 10-16C22 5.5 18 1 12 1z" fill="none" stroke="#fff" stroke-width="2.5"/><circle cx="12" cy="11" r="4" fill="#fff"/></svg>
    <span>Palm Shore, Florida</span>
  </div>
  <div class="abs contact-line center-x" style="left:597px; top:720px; font-size:29px;">
    <svg class="icon" width="26" height="26" viewBox="0 0 26 26"><circle cx="13" cy="13" r="12" fill="#fff"/><rect x="6.5" y="8.5" width="13" height="9" fill="none" stroke="#000" stroke-width="1.8"/><path d="M6.5 8.5l6.5 5 6.5-5" fill="none" stroke="#000" stroke-width="1.8"/></svg>
    <span>Service@BriskFixers24.com</span>
  </div>
</section>

<!-- BACK -->
<section class="card card-back" aria-label="Postcard back">
  <svg class="layer" viewBox="0 0 1170 787" width="1170" height="787" aria-hidden="true">
    <polygon points="0,0 932,0 932,217 23,217 23,642 236,642 236,787 0,787" fill="#000"/>
  </svg>

  <div class="brand-mark" style="left:22px; top:25px; width:168px; height:168px; font-size:22px;">BRISK<br>FIXERS 24</div>

  <div class="abs brand-title center-x" style="left:486px; top:18px; font-size:58px;">BRISK FIXERS 24</div>
  <div class="title-rule" style="left:280px; width:412px; top:80px;"></div>
  <div class="abs brand-sub center-x" style="left:486px; top:88px; font-size:46px;">HANDYMAN</div>
  <div class="abs web-line center-x" style="left:486px; top:155px; font-size:36px;">
    <svg class="icon" width="38" height="38" viewBox="0 0 40 40" fill="none" stroke="#fff200" stroke-width="3"><circle cx="20" cy="20" r="17"/><ellipse cx="20" cy="20" rx="8" ry="17"/><line x1="3" y1="20" x2="37" y2="20"/><line x1="6" y1="11" x2="34" y2="11"/><line x1="6" y1="29" x2="34" y2="29"/></svg>
    <span>BriskFixers24.com</span>
  </div>

  <svg class="partner-badge" style="left:705px; top:22px;" width="210" height="180" viewBox="0 0 210 180" aria-hidden="true">
    <circle cx="105" cy="92" r="82" fill="#fff"/>
    <circle cx="105" cy="92" r="74" fill="#2b3a7a"/>
    <rect x="0" y="100" width="210" height="30" fill="#d81f26"/>
  </svg>

  <div class="photo-tile tile-welding" role="img" aria-label="Photo of metal fabrication with welding sparks" style="left:23px; top:217px; width:311px; height:208px;"></div>
  <div class="photo-tile tile-router" role="img" aria-label="Photo of a wifi router beside a laptop and phone" style="left:334px; top:217px; width:308px; height:208px;"></div>
  <div class="photo-tile tile-cables" role="img" aria-label="Photo of a frustrated person tangled in computer cables" style="left:23px; top:425px; width:311px; height:217px;"></div>
  <div class="photo-tile tile-frames" role="img" aria-label="Photo of picture frames hung on a wall above a desk" style="left:334px; top:425px; width:308px; height:217px;"></div>

  <div class="abs cta center-x" style="left:118px; top:657px; font-size:24px;"><span class="cta-word">TEXT</span> TO INQUIRE</div>
  <div class="abs contact-line center-x" style="left:118px; top:686px; font-size:16px; gap:5px;">
    <svg class="icon" width="16" height="16" viewBox="0 0 26 26"><circle cx="13" cy="13" r="12" fill="#fff"/><path d="M8 7c1-1 2-1 2.6 0l1.2 2c.4.7.2 1.3-.4 1.8l-.8.6c.6 1.6 1.8 2.9 3.4 3.6l.6-.8c.5-.6 1.1-.8 1.8-.4l2 1.2c1 .6 1 1.6 0 2.6-1.3 1.3-3 1.4-5 .3-2.6-1.4-4.5-3.4-5.8-6-1-2-.9-3.6.4-4.9z" fill="#000"/></svg>
    <span>(555) 014 2290</span>
  </div>
  <div class="abs contact-line center-x" style="left:118px; top:708px; font-size:16px; gap:5px;">
    <svg class="icon" width="14" height="16" viewBox="0 0 24 28"><path d="M12 1C6 1 2 5.5 2 11c0 7 10 16 10 16s10-9 10-16C22 5.5 18 1 12 1z" fill="none" stroke="#fff" stroke-width="3"/><circle cx="12" cy="11" r="4" fill="#fff"/></svg>
    <span>Palm Shore, Florida</span>
  </div>
  <div class="abs contact-line center-x" style="left:118px; top:730px; font-size:16px; gap:5px;">
    <svg class="icon" width="16" height="16" viewBox="0 0 26 26"><circle cx="13" cy="13" r="12" fill="#fff"/><rect x="6.5" y="8.5" width="13" height="9" fill="none" stroke="#000" stroke-width="1.8"/><path d="M6.5 8.5l6.5 5 6.5-5" fill="none" stroke="#000" stroke-width="1.8"/></svg>
    <span>Service@BriskFixers24.com</span>
  </div>
</section>

</body>
</html>
```